Business Card Design Project

Beauty Therapist
Bold, bright, feminine, like contrast, love flowers, girly stuff. Must be beautiful. But open to all suggestions. Business name: Plush Clover.
xxx
Danuta Kaczmarczyk
Updates

Project Deadline Extended
Reason: I think you need more time to design something good. X

Target Market(s)

ignore this

Industry/Entity Type

Business

```html
<!DOCTYPE html>
<html lang="en">
<head>
<meta charset="utf-8">
<title>Plush Clover – Business Cards</title>
<link rel="stylesheet" href="https://fonts.googleapis.com/css2?family=Open+Sans:ital,wght@0,400;0,700;1,700&family=Satisfy&display=swap">
<style>
  :root {
    --backdrop: #0e0e0e;
    --plum-deep: #1d0005;
    --plum-dark: #2a0309;
    --wine: #4f1c1f;
    --wine-low: #3c1216;
    --magenta: #7c0c4c;
    --berry-pink: #e3177d;
    --tangerine: #f05a22;
    --crimson: #c8103c;
    --rose: #e2356a;
    --olive: #5a3c0a;
    --olive-warm: #7a4a12;
  }
  * { margin: 0; padding: 0; box-sizing: border-box; }
  html, body {
    width: 1200px; height: 900px; overflow: hidden;
    background: var(--backdrop);
  }
  .card {
    position: absolute; left: 370px; width: 450px; height: 268px; display: block;
  }
  .card--front { top: 133px; }
  .card--back { top: 452px; }
  .contact-name { font-family: "Satisfy", cursive; font-size: 15px; fill: var(--berry-pink); }
  .contact-role { font-family: "Open Sans", sans-serif; font-size: 8.5px; font-weight: 700; font-style: italic; fill: var(--berry-pink); }
  .contact-line { font-family: "Open Sans", sans-serif; font-size: 8.5px; font-weight: 700; fill: var(--tangerine); }
  .brand-name { font-family: "Open Sans", sans-serif; font-weight: 700; fill: var(--tangerine); }
  .brand-name--small { font-size: 14px; }
  .brand-name--large { font-size: 29px; }
  .brand-dot { fill: var(--berry-pink); }
</style>
</head>
<body>

<svg class="card card--front" viewBox="0 0 450 268" aria-label="Business card front with contact details">
  <defs>
    <linearGradient id="wine-fade" x1="0" y1="0" x2="0" y2="1">
      <stop offset="0" stop-color="var(--wine)"/>
      <stop offset="1" stop-color="var(--wine-low)"/>
    </linearGradient>
    <linearGradient id="plum-fade" x1="0" y1="0" x2="0" y2="1">
      <stop offset="0" stop-color="var(--plum-dark)"/>
      <stop offset="1" stop-color="var(--plum-deep)"/>
    </linearGradient>
  </defs>
  <rect class="panel-right" width="450" height="268" fill="url(#wine-fade)"/>
  <path class="panel-left" d="M0 0 H232 C200 30 196 70 212 120 C228 175 236 220 214 268 H0 Z" fill="url(#plum-fade)"/>
  <path class="wave-band" d="M232 0 C200 30 196 70 212 120 C228 175 236 220 214 268" fill="none" stroke="var(--magenta)" stroke-width="7"/>

  <text class="contact-name" x="177" y="156" text-anchor="end">Danuta Kaczmarczyk</text>
  <text class="contact-role" x="177" y="168" text-anchor="end">Position</text>
  <text class="contact-line" x="177" y="180" text-anchor="end">hello@plushclover.com</text>
  <text class="contact-line" x="177" y="202" text-anchor="end">Phone:  555 210 4417</text>
  <text class="contact-line" x="177" y="214" text-anchor="end">Fax: 555 210 4418</text>
  <text class="contact-line" x="177" y="226" text-anchor="end">www.plushclover.com</text>

  <circle class="brand-dot" cx="272" cy="137" r="7"/>
  <text class="brand-name brand-name--small" x="284" y="142">Plush Clover</text>
</svg>

<svg class="card card--back" viewBox="0 0 450 268" aria-label="Business card back with brand name">
  <defs>
    <linearGradient id="wine-fade-back" x1="0" y1="0" x2="0" y2="1">
      <stop offset="0" stop-color="var(--wine)"/>
      <stop offset="1" stop-color="var(--wine-low)"/>
    </linearGradient>
    <linearGradient id="foliage-tone" x1="0" y1="0" x2="1" y2="1">
      <stop offset="0" stop-color="var(--olive-warm)"/>
      <stop offset="1" stop-color="var(--olive)"/>
    </linearGradient>
  </defs>
  <rect class="panel-right" width="450" height="268" fill="url(#wine-fade-back)"/>
  <rect class="foliage-area" width="150" height="268" fill="url(#foliage-tone)" role="img" aria-label="Pattern of autumn leaves in orange and olive tones"/>
  <path class="band band--crimson" d="M118 0 H150 C130 60 128 140 150 268 H140 C110 170 108 70 118 0 Z" fill="var(--crimson)" opacity="0.8"/>
  <path class="band band--rose" d="M138 0 H146 V268 H140 C136 180 132 90 138 0 Z" fill="var(--rose)"/>

  <circle class="brand-dot" cx="186" cy="138" r="14"/>
  <text class="brand-name brand-name--large" x="206" y="148">Plush Clover</text>
</svg>

</body>
</html>
```